ZRM Pty Ltd business card

we need to get a business card designed. We're a large whole seller of baby formula , health supplement and cosmetic products.

Target Market(s)

Big online E commerce platforms, supermarket channels in Asia.

Industry/Entity Type

Business

Contact Information for Business Card

glossy

Logo Text

ZRM

Colors
abd036

Requirements
Must have
• ZRM

```html
<!DOCTYPE html>
<html lang="en">
<head>
<meta charset="utf-8">
<title>ZRM Pty Ltd – Business Card</title>
<link rel="stylesheet" href="https://fonts.googleapis.com/css2?family=Arimo:wght@400;700&display=swap">
<style>
  :root {
    --brand-green: #abd036;
    --ink: #2b2b2b;
    --card-white: #fbfbfb;
    --backdrop: #2a2a2a;
    --photo-warm: #e9dccb;
    --photo-rose: #dcb8b0;
    --photo-sage: #b9cdb8;
  }
  * { box-sizing: border-box; margin: 0; padding: 0; }
  html, body {
    width: 1200px; height: 873px; overflow: hidden;
    background: var(--backdrop);
    font-family: "Arimo", Arial, sans-serif;
  }
  .stage { position: relative; width: 1200px; height: 873px; }
  .card {
    position: absolute; top: 281px;
    width: 540px; height: 310px;
    background: var(--card-white);
    border-radius: 18px;
    overflow: hidden;
  }
  .card--front { left: 40px; }
  .card--back  { left: 620px; }

  .card__band { position: absolute; inset: 0; }

  .wordmark {
    position: absolute;
    font-family: "Arimo", Arial, sans-serif;
    font-weight: 700;
    color: var(--brand-green);
    letter-spacing: 2px;
    line-height: 1;
  }
  .card--front .wordmark { left: 120px; top: 48px; font-size: 60px; }
  .card--back .wordmark  { left: 0; right: 0; top: 24px; text-align: center; font-size: 58px; }

  .company-address {
    position: absolute; right: 30px; top: 104px;
    font-style: normal;
    text-align: right; font-size: 13px; line-height: 1.45; color: var(--ink);
  }
  .company-address__name { color: var(--brand-green); }

  .contact {
    position: absolute; left: 0; top: 240px;
    display: flex; align-items: stretch;
  }
  .contact__tab {
    width: 26px; background: var(--brand-green);
    border-radius: 0 8px 8px 0;
    display: flex; flex-direction: column; justify-content: space-around; align-items: center;
    padding: 4px 0;
  }
  .contact__list {
    list-style: none; padding-left: 12px;
    font-size: 13px; line-height: 20px; color: var(--ink);
  }

  .product-photo {
    position: absolute; left: 30px; top: 95px; width: 480px; height: 145px;
    border-radius: 6px;
    background: linear-gradient(90deg, var(--photo-warm), var(--photo-rose) 45%, var(--photo-sage) 75%, var(--photo-warm));
  }
  .tagline {
    position: absolute; left: 0; right: 0; bottom: 26px;
    text-align: center; font-size: 20px; letter-spacing: 0.5px;
    color: var(--brand-green);
  }
</style>
</head>
<body>
<main class="stage">

  <section class="card card--front" aria-label="Business card front">
    <svg class="card__band" width="540" height="310" viewBox="0 0 540 310">
      <polygon points="0,200 540,30 540,50 0,220" fill="var(--brand-green)"/>
      <g transform="translate(305 114) rotate(-17.5)">
        <text x="0" y="4.5" text-anchor="middle" font-family="Arimo, Arial, sans-serif" font-weight="700" font-size="12.5" fill="#ffffff" letter-spacing="0.5">CLARA WHITFIELD</text>
        <text x="0" y="21" text-anchor="middle" font-family="Arimo, Arial, sans-serif" font-size="9" fill="var(--brand-green)" letter-spacing="0.5">FOUNDER &amp; CEO</text>
      </g>
    </svg>

    <div class="wordmark">ZRM</div>

    <address class="company-address">
      <div class="company-address__name">ZRM PTY LTD.</div>
      <div>PO Box 5280</div>
      <div>Eastwood QLD 4102</div>
    </address>

    <div class="contact">
      <div class="contact__tab">
        <svg width="12" height="12" viewBox="0 0 12 12" aria-label="Phone">
          <path d="M2.5 1 L4.5 1 L5.2 3.6 L3.9 4.6 Q5 7 7.4 8.1 L8.4 6.8 L11 7.5 L11 9.5 Q10.5 11 9 11 Q1 10 1 2.5 Q1 1 2.5 1 Z" fill="#ffffff"/>
        </svg>
        <svg width="12" height="10" viewBox="0 0 12 10" aria-label="Email">
          <rect x="0.5" y="1" width="11" height="8" fill="none" stroke="#ffffff" stroke-width="1.2"/>
          <polyline points="0.5,1 6,5.5 11.5,1" fill="none" stroke="#ffffff" stroke-width="1.2"/>
        </svg>
        <svg width="11" height="11" viewBox="0 0 11 11" aria-label="Messaging">
          <circle cx="5.5" cy="5.5" r="5" fill="#ffffff"/>
        </svg>
      </div>
      <ul class="contact__list">
        <li>0400 215 786</li>
        <li>info@zrm-example.com</li>
        <li>Clara.zrm</li>
      </ul>
    </div>
  </section>

  <section class="card card--back" aria-label="Business card back">
    <div class="wordmark">ZRM</div>
    <div class="product-photo" role="img" aria-label="Product range photograph: bottles, jars, compacts and tubes of health supplement and cosmetic products"></div>
    <p class="tagline">HEALTH SUPPLEMENT &amp; COSMETIC PRODUCTS.</p>
  </section>

</main>
</body>
</html>
```